Past Cedar Hills Oz Tour Flyer

I need a dynamic flyer for a concert tour.
I have uploaded the file. Please use these ingredients for the design.
The font for the title is Jellyka Jellyfish lower case from www.glyphmarket-demo.net
Updates
We are getting close!! We just need bright colours, the headings to STAND OUT and Byron Bay has to be moved to under NSW Bellingen.
Thanks for all your hard work!
Target Market(s)
We are targeting a wide range of customers from old age to children and families
Industry/Entity Type
Tour
Look and feel
Each slider illustrates characteristics of the customer's brand and the style your logo design should communicate.

```html
<!DOCTYPE html>
<html lang="en">
<head>
<meta charset="utf-8">
<title>Past Cedar Hills – Tour Flyer</title>
<link rel="stylesheet" href="https://fonts.googleapis.com/css2?family=Sacramento&family=Oswald:wght@300;400;500&family=Open+Sans:wght@400;600&display=swap">
<style>
  :root {
    --sky-top: #4a4fc0;
    --sky-violet: #b04fc4;
    --sky-deep: #2a1f66;
    --white: #ffffff;
    --heading-yellow: #ffee00;
    --tour-orange: #ff8a2a;
    --band-orange: #f08019;
    --band-black: #000000;
    --pattern-teal: #10a6b0;
    --pattern-red: #e8203c;
    --pattern-green: #3fb84a;
    --pattern-orange: #ff7a1a;
    --pattern-yellow: #ffc21a;
    --pattern-blue: #2a5fd0;
  }
  * { margin: 0; padding: 0; box-sizing: border-box; }
  html, body { width: 830px; height: 1200px; overflow: hidden; background: var(--sky-deep); }
  .flyer {
    position: relative; width: 830px; height: 1200px; overflow: hidden;
    background:
      radial-gradient(ellipse 520px 320px at 640px 40px, rgba(200,100,230,.95), transparent 70%),
      radial-gradient(ellipse 420px 300px at 170px 200px, rgba(255,150,60,.55), transparent 70%),
      radial-gradient(ellipse 500px 300px at 120px 60px, rgba(80,110,230,.8), transparent 70%),
      linear-gradient(180deg, var(--sky-top) 0%, #3a2a8a 25%, #24184f 45%, #1a2a4a 100%);
  }
  .pattern-field {
    position: absolute; left: 0; top: 470px; width: 830px; height: 525px;
    background:
      radial-gradient(ellipse 280px 240px at 310px 270px, rgba(232,32,60,1), transparent 72%),
      radial-gradient(ellipse 260px 220px at 570px 130px, rgba(63,184,74,.95), transparent 72%),
      radial-gradient(ellipse 260px 280px at 110px 330px, rgba(16,166,176,1), transparent 72%),
      radial-gradient(ellipse 260px 220px at 700px 400px, rgba(16,166,176,.9), transparent 72%),
      radial-gradient(ellipse 230px 180px at 400px 80px, rgba(255,122,26,.95), transparent 72%),
      radial-gradient(ellipse 200px 160px at 230px 120px, rgba(255,194,26,.8), transparent 72%),
      radial-gradient(ellipse 240px 200px at 520px 470px, rgba(42,95,208,.85), transparent 72%),
      linear-gradient(180deg, rgba(36,24,79,.0) 0%, #1c3556 60%, #16404f 100%);
  }
  .dancer-photo {
    position: absolute; left: 430px; top: 80px; width: 400px; height: 580px;
    background:
      radial-gradient(ellipse 150px 240px at 170px 260px, rgba(255,110,30,1), transparent 75%),
      radial-gradient(ellipse 120px 160px at 340px 280px, rgba(240,80,40,.95), transparent 75%),
      radial-gradient(ellipse 110px 90px at 200px 120px, rgba(255,200,40,.85), transparent 80%),
      radial-gradient(ellipse 160px 140px at 260px 360px, rgba(230,190,110,.7), transparent 80%);
  }
  .title {
    position: absolute; left: 48px; top: 70px;
    font-family: "Sacramento", cursive; color: var(--white);
    font-size: 128px; line-height: 110px;
  }
  .title span { display: block; }
  .title .line-two { margin-left: -6px; }
  .subtitle {
    position: absolute; left: 78px; top: 330px;
    font-family: "Oswald", sans-serif; font-weight: 400; color: var(--white);
    font-size: 38px; line-height: 48px; letter-spacing: -0.2px;
  }
  .tour-label {
    position: absolute; left: 165px; top: 384px;
    font-family: "Oswald", sans-serif; font-weight: 400; color: var(--tour-orange);
    font-size: 40px; line-height: 48px;
  }
  .region { position: absolute; }
  .region h2 {
    font-family: "Oswald", sans-serif; font-weight: 500; color: var(--heading-yellow);
    font-size: 33px; line-height: 40px; margin-bottom: 2px;
    text-shadow: 0 2px 6px rgba(0,0,0,.55);
  }
  .region li {
    list-style: none; font-family: "Open Sans", sans-serif; font-weight: 600; color: var(--white);
    font-size: 19px; line-height: 30px;
    text-shadow: 0 1px 4px rgba(0,0,0,.45);
  }
  .region-vic { left: 128px; top: 654px; }
  .region-act { left: 128px; top: 864px; }
  .region-nsw { left: 315px; top: 654px; }
  .region-qld { left: 545px; top: 728px; }
  .info-band {
    position: absolute; left: 0; top: 995px; width: 415px; height: 205px;
    background: var(--band-orange); color: var(--white);
    font-family: "Oswald", sans-serif; font-weight: 300;
    font-size: 28px; line-height: 31px; text-align: center; padding-top: 23px;
  }
  .partner-band {
    position: absolute; left: 415px; top: 995px; width: 415px; height: 205px;
    background: var(--band-black);
    display: flex; align-items: center; justify-content: center; gap: 30px;
  }
  .partner {
    display: flex; align-items: center; gap: 8px;
    font-family: "Oswald", sans-serif; font-weight: 400; color: var(--white);
    font-size: 20px; line-height: 24px;
  }
  .partner-dot { width: 14px; height: 14px; border-radius: 50%; background: var(--band-orange); flex: none; }
</style>
</head>
<body>
  <main class="flyer">
    <div class="pattern-field" role="img" aria-label="Bright colourful triangle mosaic background"></div>
    <div class="dancer-photo" role="img" aria-label="Photo of a young chorus member dancing in an orange costume with a straw skirt"></div>

    <h1 class="title"><span>Past</span><span class="line-two">Cedar Hills</span></h1>
    <p class="subtitle">The Savanna Youth Chorus</p>
    <p class="tour-label">Australia Tour</p>

    <section class="region region-vic">
      <h2>VICTORIA</h2>
      <ul><li>Geelong</li><li>Sunbury</li><li>Melbourne</li><li>Bendigo</li><li>Albury</li></ul>
    </section>
    <section class="region region-act">
      <h2>A.C.T.</h2>
      <ul><li>Canberra</li></ul>
    </section>
    <section class="region region-nsw">
      <h2>N.S.W.</h2>
      <ul><li>Nowra</li><li>Sydney</li><li>Wollongong</li><li>Blue Mountains</li><li>Port Macquarie</li><li>Laurieton</li><li>Taree</li><li>Bellingen</li><li>Byron Bay</li></ul>
    </section>
    <section class="region region-qld">
      <h2>QLD</h2>
      <ul><li>Gold Coast</li><li>Sunshine Coast</li><li>Brisbane</li></ul>
    </section>

    <footer>
      <div class="info-band">
        <p>TICKETS and info at</p>
        <p>www.chorusvoices-demo.org</p>
        <p>CONTACT:</p>
        <p>Dana Whitlow&nbsp; 0412 555 019</p>
      </div>
      <div class="partner-band">
        <div class="partner"><span class="partner-dot"></span><span>Chorus Voices</span></div>
        <div class="partner"><span class="partner-dot"></span><span>Savanna Youth Chorus</span></div>
      </div>
    </footer>
  </main>
</body>
</html>
```